Tall Petes Ember Poultry Christmas Flyer Special

We are a Charcoal Chicken and Lebanese Cusine Restaraunt both eat in and take away and offer Home Delivery services. WE are based in Merrylands in Sydney. Australia.
On the front Page I would like to offer a 2 month Promotion starting at 1st of December and last day of January 2013.
The front page will have something along the lines of :
The new Place to eat Charocal Chicken
also there will be:
Best tasting chicken in Sydney
The special will be:
Buy one whole chicken and get a Large CHips and Regular Garlic for Free. Savings of $6.50. (TAKE AWAY AND PICKUP ONLY)
Details of Address and Facebook and web address will be included.
Must be very eye catchy and graphical.
The back page will be about Dine In and text and graphics should look more Professional.
The SPecial will be on promoting the Banquet we offer here (Tall Petes Royal Feast) minimum is for 2 persons.
the banquet offers:
labni dip
raw mixed vege plate
baba ghanouj
hommous
tabouli
mixed nuts
mixed pickles
shankleesh
fried cauliflower
fried and fresh lebanese bread
kibi nayi
sambousik
cheese sambousik
fried kibi
sharawma
chicken wings
skewered kafta
skewered shish tawouk
skewered shish kebab
(IF ODERED SEPERATELY FOR 2 PEOPLE IT WOULD COST $168 BUT ONLY FOR DECEMBER AND JANUARY WILL COST 45pp. Please also note 1 free drink pp from Selected beverages.
NOTE( BYO on FLyer)
Will only recieve this special if booked over the phone.
On both pages must include details of shop and Open 7 days
I will upload images to be used with the flyer
BOTH PAGES AT THE BOTTOM IN SMALL TEXT SHOULD SAY 100% HALAL.
THIS OFFER CANNOT BE USED IN CONJUNCTION WITH THE TALL PETES REWARDS PASS.
WITH THE IMAGE AT THE FRON FOR THE CHICKEN AND CHIPS. IF POSSIBLE TO SEE IF YOU CAN FIND SOMETHING ON THE NET. MUST BE FLAT CHICKEN NOT ROUND.
Updates
i got some photos uploaded.
named back and front. so front of brouchure and back of brouchure.
and please note the price of the special at thefront which is 11.90

```html
<!DOCTYPE html>
<html lang="en">
<head>
<meta charset="utf-8">
<title>Tall Petes Ember Poultry – Summer Special</title>
<link rel="stylesheet" href="https://fonts.googleapis.com/css2?family=Anton&family=Bowlby+One+SC&family=Oswald:wght@400&family=Share+Tech+Mono&display=swap">
<style>
  :root {
    --ink: #000000;
    --teal: #1f8a96;
    --teal-light: #2aa9b5;
    --white: #ffffff;
    --red: #e3170f;
    --yellow: #fff200;
    --orange: #f7941d;
    --halal-green: #8dc63f;
    --logo-red: #e0262b;
  }
  html, body {
    margin: 0;
    padding: 0;
    overflow: hidden;
    background: var(--white);
  }
  .flyer {
    position: relative;
    width: 847px;
    height: 1200px;
    overflow: hidden;
    background: var(--ink);
  }
  .dates-band {
    position: absolute;
    left: 0; top: 0;
    width: 847px; height: 185px;
    background: var(--ink);
  }
  .dates {
    position: absolute;
    top: 48px; left: 0; width: 847px;
    margin: 0;
    text-align: center;
    font-family: "Bowlby One SC", sans-serif;
    font-size: 37px;
    line-height: 56px;
    color: var(--teal-light);
    -webkit-text-stroke: 1px var(--white);
    letter-spacing: 1px;
  }
  .hero-photo {
    position: absolute;
    left: 0; top: 185px;
    width: 847px; height: 873px;
    background:
      radial-gradient(ellipse 320px 300px at 330px 470px, #7a4a2a 0%, #5b3720 45%, rgba(91,55,32,0) 100%),
      radial-gradient(ellipse 520px 360px at 420px 640px, #f2efe9 0%, #d9d4cb 60%, rgba(217,212,203,0) 100%),
      linear-gradient(180deg, #8a6a55 0%, #a7876f 35%, #c9b7a6 70%, #6f6a60 100%);
  }
  .headline {
    position: absolute;
    left: 0; top: 240px; width: 847px;
    margin: 0;
    text-align: center;
    font-family: "Oswald", sans-serif;
    font-weight: 400;
    font-size: 88px;
    line-height: 92px;
    color: var(--teal);
    -webkit-text-stroke: 2px var(--white);
    transform: scaleX(0.82);
    letter-spacing: -2px;
  }
  .price-burst {
    position: absolute;
    left: 440px; top: 435px;
    width: 370px; height: 370px;
  }
  .price {
    position: absolute;
    left: 470px; top: 490px;
    width: 300px;
    margin: 0;
    text-align: center;
    font-family: "Anton", sans-serif;
    color: var(--yellow);
    line-height: 1;
  }
  .price-amount { display: block; font-size: 86px; letter-spacing: 2px; }
  .price-currency { display: block; font-size: 80px; margin-top: 8px; }
  .tagline {
    position: absolute;
    left: 18px; top: 566px;
    margin: 0;
    font-family: "Share Tech Mono", monospace;
    font-size: 31px;
    line-height: 34px;
    color: var(--orange);
    -webkit-text-stroke: 1px var(--white);
    font-weight: bold;
  }
  .offer {
    position: absolute;
    left: 34px; top: 744px;
    margin: 0;
    font-family: "Bowlby One SC", sans-serif;
    font-size: 23px;
    line-height: 32px;
    color: var(--white);
    -webkit-text-stroke: 1px var(--ink);
  }
  .halal-badge {
    position: absolute;
    left: 24px; top: 930px;
    width: 150px; height: 112px;
    border-radius: 50%;
    background: var(--ink);
    border: 7px solid var(--halal-green);
    box-sizing: border-box;
    transform: rotate(-28deg);
    display: flex; align-items: center; justify-content: center;
    font-family: "Share Tech Mono", monospace;
    font-size: 14px;
    color: var(--teal-light);
  }
  .brand {
    position: absolute;
    left: 492px; top: 1060px;
    width: 330px;
    display: flex; align-items: center; gap: 10px;
    font-family: "Bowlby One SC", sans-serif;
    font-size: 25px;
    line-height: 30px;
    color: var(--logo-red);
  }
  .brand-dot {
    flex: none;
    width: 26px; height: 26px;
    border-radius: 50%;
    background: var(--logo-red);
  }
  .contact-note {
    position: absolute;
    left: 34px; top: 1092px;
    margin: 0;
    font-family: "Oswald", sans-serif;
    font-size: 16px;
    line-height: 24px;
    color: var(--teal-light);
    font-weight: 400;
  }
</style>
</head>
<body>
<main class="flyer">
  <header class="dates-band">
    <p class="dates">from 1st of December to<br>the last day of January 2013</p>
  </header>

  <div class="hero-photo" role="img" aria-label="Photo of flat charcoal chicken on a white plate with fresh salad greens"></div>

  <h1 class="headline">THE NEW PLACE TO<br>EAT CHAROCAL CHICKEN</h1>

  <svg class="price-burst" viewBox="-185 -185 370 370" aria-hidden="true">
    <g fill="#e3170f">
      <circle r="152"/>
      <rect x="-127" y="-127" width="254" height="254" transform="rotate(0)"/>
      <rect x="-127" y="-127" width="254" height="254" transform="rotate(7.5)"/>
      <rect x="-127" y="-127" width="254" height="254" transform="rotate(15)"/>
      <rect x="-127" y="-127" width="254" height="254" transform="rotate(22.5)"/>
      <rect x="-127" y="-127" width="254" height="254" transform="rotate(30)"/>
      <rect x="-127" y="-127" width="254" height="254" transform="rotate(37.5)"/>
      <rect x="-127" y="-127" width="254" height="254" transform="rotate(45)"/>
      <rect x="-127" y="-127" width="254" height="254" transform="rotate(52.5)"/>
      <rect x="-127" y="-127" width="254" height="254" transform="rotate(60)"/>
      <rect x="-127" y="-127" width="254" height="254" transform="rotate(67.5)"/>
      <rect x="-127" y="-127" width="254" height="254" transform="rotate(75)"/>
      <rect x="-127" y="-127" width="254" height="254" transform="rotate(82.5)"/>
    </g>
  </svg>
  <p class="price"><span class="price-amount">11.90</span><span class="price-currency">$</span></p>

  <p class="tagline">Best tasting<br>&nbsp;chicken in Sydney</p>

  <p class="offer">Buy one whole chicken<br>and get a Large CHips and Regular Garlic<br>for Free. Savings of $6.50.<br>(TAKE AWAY AND PICKUP ONLY)</p>

  <div class="halal-badge">100% HALAL.</div>

  <div class="brand"><span class="brand-dot"></span><span>Tall Petes Ember Poultry</span></div>

  <p class="contact-note">Details of Address and Facebook and<br>web address will be included.</p>
</main>
</body>
</html>
```